UPDATE: Please see File 2 for the most recent content, the precise content to include into the design. Also, we want an image that will clearly present the 7-Step Management Process for our Framework for High Performance.

When someone clicks on any portion of the image you would design, it would open up a box that would give all of the details and subtext of that particular category. I trust you guys as designers to figure out this challenge. I am a content expert. I know the answers as to how to run a more effective business, but I don't have any idea how to effectively present my business process graphically! To be clear, these are only ideas; I need you to figure out this challenge. I know the business principles very well, but I don't know how to express them in a well designed image that can be clicked-on and then opens up to present the content under each category.

The image must be printable as well.

We need a clear, crisp way to present our unique 7-Step business process and philosophy such that executives can quickly and clearly assess our principles and business management process. We need a very professional, crisp, catchy design to incorporate our 7 categories and the written process points under each category headline.

I have attached what we are currently using, and it is not good! We print it out on a regular piece of paper and the font is too small and hard to read. Not thrilled with the colors, either. We need a totally new concept. A totally new design and process for executives to quickly and easily access this information.

This is the culmination of 35 years of consulting work, all boiled down into a single page, and candidly, the content is fantastic! But I need a MUCH better, cleaner, more crisp, more catchy and far more professional way to present this and give it to clients.

PLEASE NOTE: We will adjust some of the text or subtract or delete a word or line here or there. What is most important is your design approach to figure out how to present this quantity of information in an easy to read, easy to understand format.

I have attached updated content for you to cut and paste into your design.
Updates

I am extremely disappointed. I committed a huge budget to this project after your site "encouraged" me to go-hard on the money, which I did, and now I am getting just terrible designs. These are not what I am looking for, many have just copied my ideas without any original thought. I have sent Pixel Guild multiple messages about this and nothing is changing. Plus, your people are not seemingly reading the full brief, etc. Either just cancel the entire project or help me re-write the brief to get people to better understand, or extend this another 10 days or something. I am really at my wit's end here. Please see all of my other correspondence with you about this project. The last project went super great, so I was excited about this one, but so far, I am just so disappointed with the proposed solutions to my design challenge. Mark Venstrom markTvenstrom@mailbrook.example (555) 318-4027

Target Market(s)

Business Executives. Fortune 500 Companies. Millennials. Managers. Business Executives. INDUSTRIES: High Tech, Banking, Finance, Insurance, Pharmaceuticals, Sales Management. All high-end senior level business executives

Industry/Entity Type

Business

Logo Text

Still working on this! Need Help!

Font styles to use
Sans Serif

Colors
7fa7d0
0355a3
fef6f1
f37022
ffc214
9bcb3c
3277b5
ec1f27
fbed22

Requirements
Must have
• Professional. Crisp. Clear. Punchy. Easy to read. Easy to understand. The problem we have is that we need to retain all of these points, but it is a lot to read, I know. But these are all timeless business principles that we want our clients to be able to easily see, read and access in the moment. The current format of 8 1/2 x 11 inch paper doesn't seem to be adequate. Do we make it multiple pages, do we use a digital graphic and they can click on a particular section and then that section opens-us a box of additional text? We are open to any solution, but it must be clear, crisp, easy to read and look very highly designed, highly professional.

The graphic design is most important. it must be printable and it should be set up so that if you click on any category header, the content behind that header will open up in a pop up screen to give you all the details.
Nice to have
• A flow. A flowchart. Easy to access. Easy to understand. Serious. Professional. It should feel like: We mean Business. That this is very professional. That these principles are world class, world leading process to improve business. It should look very professional, studius, scholarly, an executive would want to see this on her desk and use this tool throughout the day. It cannot be cartoonish in any way. It cannot use clip art or silly things.
Should not have
• Cartoonish. Playful. overly- feminine looking, lacy, frilly, etc.

```html
<!DOCTYPE html>
<html lang="en">
<head>
<meta charset="utf-8">
<title>7-Step Management Process – Framework for High Performance</title>
<link rel="stylesheet" href="https://fonts.googleapis.com/css2?family=Oswald:wght@600;700&display=swap">
<style>
  :root{
    --sky:#7fa7d0;
    --navy:#0355a3;
    --orange:#f37022;
    --amber:#ffc214;
    --green:#9bcb3c;
    --steel:#3277b5;
    --red:#ec1f27;
    --yellow:#f4ea22;
    --white:#ffffff;
  }
  html,body{margin:0;padding:0;width:1200px;height:1200px;overflow:hidden;background:var(--white);}
  .process-funnel{display:block;width:1200px;height:1200px;}
  .step-label{font-family:"Oswald",sans-serif;font-weight:700;fill:var(--white);letter-spacing:.5px;}
  .icon{fill:none;stroke:currentColor;stroke-width:2.4;stroke-linecap:round;stroke-linejoin:round;}
  .icon .solid{fill:currentColor;stroke:none;}
  .icon .knock{fill:var(--white);}
  .band{filter:url(#soft-shadow);}
  .badge{fill:var(--white);filter:url(#soft-shadow);}
  .gear-hub{fill:var(--white);}
  .c-sky{color:var(--sky);fill:var(--sky);}
  .c-navy{color:var(--navy);fill:var(--navy);}
  .c-orange{color:var(--orange);fill:var(--orange);}
  .c-amber{color:var(--amber);fill:var(--amber);}
  .c-green{color:var(--green);fill:var(--green);}
  .c-steel{color:var(--steel);fill:var(--steel);}
  .c-red{color:var(--red);fill:var(--red);}
  .c-yellow{color:#d9cf10;fill:var(--yellow);}
  .funnel-rim{fill:var(--navy);}
</style>
</head>
<body>
<svg class="process-funnel" viewBox="0 0 960 960" xmlns="http://www.w3.org/2000/svg" role="img" aria-label="Seven-step management process funnel: Group Meetings, TM Weekly Touchpoint, Clear Communication, Delegation, Execution, Measurement, Follow-up, leading to Result">
  <defs>
    <filter id="soft-shadow" x="-10%" y="-20%" width="120%" height="150%">
      <feDropShadow dx="1" dy="3" stdDeviation="2.5" flood-color="#000" flood-opacity=".25"/>
    </filter>

    <g id="gear">
      <circle r="40"/>
      <g>
        <rect x="-7" y="-50" width="14" height="16" rx="2"/>
        <rect x="-7" y="-50" width="14" height="16" rx="2" transform="rotate(36)"/>
        <rect x="-7" y="-50" width="14" height="16" rx="2" transform="rotate(72)"/>
        <rect x="-7" y="-50" width="14" height="16" rx="2" transform="rotate(108)"/>
        <rect x="-7" y="-50" width="14" height="16" rx="2" transform="rotate(144)"/>
        <rect x="-7" y="-50" width="14" height="16" rx="2" transform="rotate(180)"/>
        <rect x="-7" y="-50" width="14" height="16" rx="2" transform="rotate(216)"/>
        <rect x="-7" y="-50" width="14" height="16" rx="2" transform="rotate(252)"/>
        <rect x="-7" y="-50" width="14" height="16" rx="2" transform="rotate(288)"/>
        <rect x="-7" y="-50" width="14" height="16" rx="2" transform="rotate(324)"/>
      </g>
    </g>

    <g id="person" class="solid">
      <circle cx="0" cy="-4" r="3.6"/>
      <path d="M-6.5 6.5a6.5 6.5 0 0 1 13 0z"/>
    </g>

    <g id="i-chart" class="icon">
      <rect x="-13" y="-14" width="22" height="26" rx="2"/>
      <polyline points="-9,4 -4,-3 0,1 5,-8"/>
      <circle class="knock" cx="8" cy="8" r="7"/>
      <path d="M8 4v4h3"/>
    </g>

    <g id="i-gauge" class="icon">
      <path d="M-15 8a15 15 0 1 1 30 0"/>
      <path d="M-11 -3l3 1M0 -7v3M11 -3l-3 1"/>
      <path d="M0 8L8 -6"/>
      <circle class="solid" cx="0" cy="8" r="2.6"/>
    </g>

    <g id="i-swap" class="icon">
      <use href="#person" transform="translate(-9 -5) scale(.9)"/>
      <use href="#person" transform="translate(9 8) scale(.9)"/>
      <path d="M2 -12a11 11 0 0 1 11 8"/>
      <polyline points="10,-6 13,-3 15,-7"/>
      <path d="M-2 13a11 11 0 0 1 -11 -7"/>
      <polyline points="-10,5 -13,3 -15,7"/>
    </g>

    <g id="i-team" class="icon">
      <use href="#person" transform="translate(-10 3) scale(.9)"/>
      <use href="#person" transform="translate(10 3) scale(.9)"/>
      <path d="M-5 -11a8 8 0 0 1 10 0"/>
      <polyline points="2,-14 5,-11 2,-8"/>
      <path d="M5 15a8 8 0 0 1 -10 0"/>
      <polyline points="-2,12 -5,15 -2,18"/>
    </g>

    <g id="i-network" class="icon">
      <circle r="12"/>
      <use href="#person" transform="scale(.8)"/>
      <use href="#person" transform="translate(0 -13) scale(.6)"/>
      <use href="#person" transform="translate(11 -6) scale(.6)"/>
      <use href="#person" transform="translate(11 7) scale(.6)"/>
      <use href="#person" transform="translate(0 14) scale(.6)"/>
      <use href="#person" transform="translate(-11 7) scale(.6)"/>
      <use href="#person" transform="translate(-11 -6) scale(.6)"/>
    </g>

    <g id="i-point" class="icon">
      <rect x="-15" y="-9" width="14" height="18" rx="1.5"/>
      <path d="M-12 -4h8M-12 0h8M-12 4h8"/>
      <path d="M2 0h12"/>
      <polyline points="10,-4 14,0 10,4"/>
    </g>

    <g id="i-org" class="icon">
      <use href="#person" transform="translate(0 -8) scale(.85)"/>
      <use href="#person" transform="translate(-11 10) scale(.75)"/>
      <use href="#person" transform="translate(11 10) scale(.75)"/>
      <path d="M-11 2v-2h22v2"/>
    </g>

    <g id="i-target" class="icon">
      <circle r="14"/>
      <circle r="9"/>
      <circle class="solid" r="3.5"/>
      <path d="M0 0L14 -14"/>
      <path d="M11 -17v6h6"/>
    </g>
  </defs>

  <!-- Funnel bands -->
  <g class="funnel-bands">
    <path class="band c-yellow" d="M95,252 L570,252 C595,252 585,278 615,278 L844,278 A31 31 0 0 1 844,340 L575,340 C545,340 555,368 530,368 L132,368 Z"/>
    <path class="band c-navy" d="M132,372 L530,372 C555,372 545,383 575,383 L851.5,383 A23.5 23.5 0 0 1 851.5,430 L540,430 C510,430 520,445 495,445 L160,445 Z"/>
    <path class="band c-green" d="M162,450 L495,450 C520,450 510,460 540,460 L852.5,460 A22.5 22.5 0 0 1 852.5,505 L510,505 C480,505 490,517 465,517 L185,517 Z"/>
    <path class="band c-amber" d="M188,522 L465,522 C490,522 480,533 510,533 L854,533 A21 21 0 0 1 854,575 L485,575 C455,575 465,585 440,585 L212,585 Z"/>
    <path class="band c-steel" d="M214,590 L440,590 C465,590 455,605 485,605 L855,605 A20 20 0 0 1 855,645 L460,645 C430,645 440,655 415,655 L232,655 Z"/>
    <path class="band c-red" d="M234,660 L415,660 C440,660 430,675 460,675 L856.5,675 A18.5 18.5 0 0 1 856.5,712 L445,712 C415,712 425,715 400,715 L248,715 Z"/>
    <path class="band c-sky" d="M250,722 L405,722 C430,722 420,742 450,742 L853.5,742 A21.5 21.5 0 0 1 853.5,785 L445,785 C415,785 425,790 400,790 L258,790 Z"/>
    <path class="band c-orange" d="M235,797 L390,797 C415,797 405,830 435,830 L845,830 A30 30 0 0 1 845,890 L300,890 Z"/>
  </g>

  <!-- Funnel rim -->
  <ellipse class="funnel-rim" cx="330" cy="215" rx="245" ry="48"/>

  <!-- Gears -->
  <g class="gears">
    <g class="gear c-sky" transform="translate(258 108) scale(.84)"><use href="#gear"/><circle class="gear-hub" r="29"/><use href="#i-chart" transform="scale(1.15)"/></g>
    <g class="gear c-navy" transform="translate(415 135) scale(.8)"><use href="#gear"/><circle class="gear-hub" r="29"/><use href="#i-swap" transform="scale(1.15)"/></g>
    <g class="gear c-red" transform="translate(342 150) scale(.88)"><use href="#gear"/><circle class="gear-hub" r="29"/><use href="#i-gauge" transform="scale(1.15)"/></g>
    <g class="gear c-amber" transform="translate(458 205) scale(.88)"><use href="#gear"/><circle class="gear-hub" r="29"/><use href="#i-org" transform="scale(1.15)"/></g>
    <g class="gear c-steel" transform="translate(380 222) scale(.8)"><use href="#gear"/><circle class="gear-hub" r="29"/><use href="#i-point" transform="scale(1.15)"/></g>
    <g class="gear c-green" transform="translate(195 215) scale(.88)"><use href="#gear"/><circle class="gear-hub" r="29"/><use href="#i-team" transform="scale(1.15)"/></g>
    <g class="gear c-yellow" transform="translate(290 228) scale(1.04)"><use href="#gear"/><circle class="gear-hub" r="29"/><use href="#i-network" transform="scale(1.2)"/></g>
  </g>

  <!-- Step labels -->
  <g class="step-labels">
    <text class="step-label" x="200" y="340" font-size="30" textLength="265" lengthAdjust="spacingAndGlyphs">GROUP MEETINGS</text>
    <text class="step-label" x="158" y="414" font-size="27" textLength="339" lengthAdjust="spacingAndGlyphs">TMWEEKLYTOUCHPOINT</text>
    <text class="step-label" x="187" y="498" font-size="23" textLength="280" lengthAdjust="spacingAndGlyphs">CLEAR COMMUNICATION</text>
    <text class="step-label" x="238" y="572" font-size="27" textLength="174" lengthAdjust="spacingAndGlyphs">DELEGATION</text>
    <text class="step-label" x="260" y="638" font-size="24" textLength="142" lengthAdjust="spacingAndGlyphs">EXECUTION</text>
    <text class="step-label" x="253" y="703" font-size="17" textLength="153" lengthAdjust="spacingAndGlyphs">MEASUREMENT</text>
    <text class="step-label" x="260" y="778" font-size="21" textLength="137" lengthAdjust="spacingAndGlyphs">FOLLOW-UP</text>
    <text class="step-label" x="305" y="846" font-size="18" textLength="80" lengthAdjust="spacingAndGlyphs">RESULT</text>
  </g>

  <!-- Step badges -->
  <g class="step-badges">
    <g class="c-yellow" transform="translate(845 309)"><circle class="badge" r="26"/><use href="#i-network" transform="scale(1.05)"/></g>
    <g class="c-navy" transform="translate(845 406)"><circle class="badge" r="22"/><use href="#i-swap" transform="scale(.9)"/></g>
    <g class="c-green" transform="translate(845 482)"><circle class="badge" r="20"/><use href="#i-team" transform="scale(.8)"/></g>
    <g class="c-amber" transform="translate(845 554)"><circle class="badge" r="18"/><use href="#i-org" transform="scale(.72)"/></g>
    <g class="c-steel" transform="translate(845 625)"><circle class="badge" r="17"/><use href="#i-point" transform="scale(.68)"/></g>
    <g class="c-red" transform="translate(845 693)"><circle class="badge" r="16"/><use href="#i-gauge" transform="scale(.65)"/></g>
    <g class="c-sky" transform="translate(845 763)"><circle class="badge" r="17"/><use href="#i-chart" transform="scale(.68)"/></g>
    <g class="c-orange" transform="translate(845 860)"><circle class="badge" r="28"/><use href="#i-target" transform="scale(1.2)"/></g>
  </g>
</svg>
</body>
</html>
```